Wendlow Cellars -responsive, bootstrap website design

Looking to build a responsive service website.

Logo and pictures have been provided.

PLEASE REVIEW ATTACHED DESIGN STYLE GUIDES & CLIENT CREATIVE BRIEF FOR OUR REQUIREMENT. THANK YOU AND GOOD LUCK!

```html
<!DOCTYPE html>
<html lang="en">
<head>
<meta charset="utf-8">
<title>Wendlow Cellars</title>
<link rel="stylesheet" href="https://fonts.googleapis.com/css2?family=Open+Sans:wght@400;600&family=Tinos:wght@400;700&display=swap">
<style>
  :root {
    --wine-red: #a5121a;
    --btn-top: #c8161f;
    --btn-bottom: #850a10;
    --panel-grey: #e6e6e6;
    --ink: #111;
    --body-ink: #333;
    --muted: #666;
    --white: #fff;
    --serif: "Tinos", "Times New Roman", serif;
    --sans: "Open Sans", Arial, sans-serif;
  }
  * { box-sizing: border-box; margin: 0; padding: 0; }
  html, body { width: 1042px; height: 1200px; overflow: hidden; }
  body { position: relative; font-family: var(--sans); color: var(--ink); }

  .hero-backdrop {
    position: absolute; inset: 0;
    background: linear-gradient(180deg, #d6961a 0%, #e6b53a 14%, #f2cd5e 26%, #c9a04a 33%, #6b5a2a 42%, #4a5222 55%, #3a4a1c 70%, #1e2a12 88%, #111a0b 100%);
  }

  .brand {
    position: absolute; left: 419px; top: 17px; width: 204px; height: 155px;
    display: flex; align-items: center; justify-content: center;
    font-family: var(--serif); font-size: 30px; color: #2a1d0c; text-align: center; line-height: 1.1;
  }

  .main-nav {
    position: absolute; left: 78px; top: 199px; width: 886px; height: 45px;
    background: var(--white);
  }
  .main-nav a {
    position: absolute; top: 14px; font-size: 12px; color: var(--ink); text-decoration: none;
  }
  .main-nav a.is-active { color: var(--wine-red); }
  .search-toggle {
    position: absolute; right: 18px; top: 0; width: 36px; height: 45px; background: #dedede;
    display: flex; align-items: center; justify-content: center;
  }

  .welcome-panel {
    position: absolute; left: 78px; top: 318px; width: 505px; height: 221px;
    background: rgba(40, 30, 15, 0.55);
    clip-path: polygon(10px 0, 495px 0, 505px 10px, 505px 211px, 495px 221px, 10px 221px, 0 211px, 0 10px);
    color: var(--white);
  }
  .welcome-panel h1 {
    position: absolute; left: 18px; top: 14px; font-family: var(--serif); font-weight: 400; font-size: 25px; white-space: nowrap;
  }
  .welcome-panel h1 strong { font-weight: 700; }
  .welcome-panel p {
    position: absolute; left: 18px; top: 68px; width: 470px;
    font-family: var(--serif); font-size: 12.2px; line-height: 21px;
  }

  .btn {
    position: absolute; width: 114px; height: 28px; border-radius: 14px;
    background: linear-gradient(180deg, var(--btn-top), var(--btn-bottom));
    color: var(--white); font-family: var(--serif); font-size: 13px;
    display: flex; align-items: center; justify-content: center; text-decoration: none;
  }

  .section { position: absolute; }
  .section h2 {
    position: absolute; font-family: var(--serif); font-weight: 400; white-space: nowrap; text-transform: uppercase;
  }
  .section p.copy {
    position: absolute; font-family: var(--serif); font-size: 12.2px; line-height: 21px; color: var(--body-ink);
  }

  .buy-wine { left: 78px; top: 622px; width: 577px; height: 236px; background: var(--white); }
  .buy-wine h2 { left: 21px; top: 32px; font-size: 23.5px; color: var(--wine-red); }
  .buy-wine p.copy { left: 21px; top: 78px; width: 385px; }
  .bottles-photo {
    position: absolute; left: 425px; top: 5px; width: 131px; height: 222px;
    background: linear-gradient(90deg, transparent 0%, #1a1416 8%, #2b2224 45%, #1a1416 92%, transparent 100%);
    border-radius: 16px 16px 6px 6px;
  }

  .recent-posts { left: 655px; top: 622px; width: 309px; height: 236px; background: var(--panel-grey); }
  .recent-posts h2 { left: 22px; top: 8px; font-size: 25px; color: var(--ink); }
  .post { position: absolute; left: 22px; width: 280px; height: 50px; }
  .post-thumb {
    position: absolute; left: 0; top: 0; width: 63px; height: 47px;
    background: linear-gradient(180deg, #b86a5a 0%, #6a2a2a 45%, #1a1414 100%);
  }
  .post-title { position: absolute; left: 74px; top: -1px; width: 210px; font-size: 11.5px; line-height: 15px; color: var(--ink); }
  .post-date { position: absolute; left: 74px; top: 35px; font-size: 11px; color: var(--ink); }
  .view-all { position: absolute; left: 23px; top: 204px; font-family: var(--serif); font-size: 13px; color: var(--wine-red); text-decoration: none; }

  .newsletter { left: 78px; top: 875px; width: 309px; height: 236px; background: var(--panel-grey); }
  .newsletter h2 { left: 19px; top: 24px; font-size: 24px; color: var(--ink); }
  .newsletter .lead { position: absolute; left: 20px; top: 64px; font-size: 11.5px; color: var(--ink); }
  .field {
    position: absolute; left: 18px; width: 255px; height: 33px; border-radius: 17px; background: var(--white);
    font-size: 11px; color: #777; padding: 9px 13px;
  }

  .every-sip { left: 387px; top: 875px; width: 577px; height: 236px; background: var(--white); }
  .every-sip h2 { left: 24px; top: 24px; font-size: 27px; color: var(--wine-red); }
  .every-sip p.copy { left: 25px; top: 82px; width: 395px; }
  .pour-photo {
    position: absolute; left: 425px; top: 24px; width: 152px; height: 195px;
    background: radial-gradient(ellipse at 40% 70%, #8a1018 0%, #b82030 30%, rgba(255,255,255,0) 65%);
  }

  .site-footer { position: absolute; left: 78px; top: 1129px; width: 886px; height: 41px; background: var(--white); }
  .site-footer small { position: absolute; left: 19px; top: 14px; font-size: 10.5px; color: var(--muted); }
  .social { position: absolute; top: 14px; width: 13px; height: 13px; border-radius: 50%; background: #555; }
</style>
</head>
<body>
  <div class="hero-backdrop" role="img" aria-label="Vineyard rows on rolling hills under a golden sunset sky"></div>

  <div class="brand">Wendlow Cellars</div>

  <nav class="main-nav">
    <a class="is-active" style="left:26px">HOME</a>
    <a style="left:130px">ABOUT</a>
    <a style="left:242px">WINES</a>
    <a style="left:351px">STORE</a>
    <a style="left:460px">NEWS</a>
    <a style="left:565px">CONTACT US</a>
    <span class="search-toggle">
      <svg width="16" height="16" viewBox="0 0 16 16"><circle cx="6.5" cy="6.5" r="4.8" fill="none" stroke="#111" stroke-width="2"/><line x1="10" y1="10" x2="14.5" y2="14.5" stroke="#111" stroke-width="2.4" stroke-linecap="round"/></svg>
    </span>
  </nav>

  <section class="welcome-panel">
    <h1>WELCOME TO <strong>WENDLOW CELLARS</strong></h1>
    <p>As Ashgrove has officially affirmed its place as one of the premier wine producing regions in the world, I was more than eager to become a part of its ever growing wine tradition For me, the wines of Ashgrove honor the distinct terroir and fruit that make for some of the most well crafted, complexity-driven and lovely wines made today.</p>
    <a class="btn" style="left:18px;top:179px">Read More</a>
  </section>

  <section class="section buy-wine">
    <h2>Buy Wendlow Cellars Wine</h2>
    <p class="copy">Lorem ipsum dolor sit amet, consectetuer adipiscing elit, sed diam nonummy nibh euismod tincidunt ut laoreet dolore magna aliquam erat volutpat. Ut wisi enim ad minim veniam, quis nostrud exerci tation ullamcorper suscipit lobortis nisl ut aliquip ex ea commodo consequat.</p>
    <a class="btn" style="left:18px;top:188px">Read More</a>
    <div class="bottles-photo" role="img" aria-label="Three bottles of red wine with cream labels"></div>
  </section>

  <aside class="section recent-posts">
    <h2>Recent Blog Posts</h2>
    <div class="post" style="top:55px">
      <div class="post-thumb" role="img" aria-label="Wine bottle at dusk"></div>
      <div class="post-title">Wendlow Cellars welcomes Owen Harley to the Wendlow Family</div>
      <div class="post-date">25/06/2014</div>
    </div>
    <div class="post" style="top:133px">
      <div class="post-thumb" role="img" aria-label="Wine bottle at dusk"></div>
      <div class="post-title">Wendlow Cellars welcomes Owen Harley to the Wendlow Family</div>
      <div class="post-date">25/06/2014</div>
    </div>
    <a class="view-all">View All...</a>
  </aside>

  <section class="section newsletter">
    <h2>News Letter Signup</h2>
    <span class="lead">Subscribe To Our News Letter</span>
    <div class="field" style="top:93px">Name</div>
    <div class="field" style="top:140px">Email</div>
    <a class="btn" style="left:19px;top:192px">Subscribe</a>
  </section>

  <section class="section every-sip">
    <h2>Every Sip Changes Lives</h2>
    <p class="copy">Lorem ipsum dolor sit amet, consectetuer adipiscing elit, sed diam nonummy nibh euismod tincidunt ut laoreet dolore magna aliquam erat volutpat. Ut wisi enim ad minim veniam, quis nostrud exerci tation ullamcorper suscipit lobortis nisl ut aliquip ex ea commodo consequat.</p>
    <a class="btn" style="left:23px;top:182px">Read More</a>
    <div class="pour-photo" role="img" aria-label="Red wine pouring from a bottle into a glass"></div>
  </section>

  <footer class="site-footer">
    <small>copyright© 2014 Wendlow Cellars. All Rights Reserved</small>
    <span class="social" style="left:755px"></span>
    <span class="social" style="left:788px"></span>
    <span class="social" style="left:821px"></span>
    <span class="social" style="left:855px"></span>
  </footer>
</body>
</html>
```